Top business card designs - show off your work!

Calling all [url removed, login to view] designers! We are giving away $1000 to the best business card design on [url removed, login to view]!

Why enter? 2 reasons:
1) $1000 main prize for the best design
2) The chance to show off your best designs to prospective employers - we will not be sealing the contest.

Here's the rules:
1) Designs should not infringe on the copyright of any existing company or designer
2) Designs should not include real personal details (use fake names and details like John Smith)
3) You may include designs you have done for previous clients

Good luck!!!

```html
<!DOCTYPE html>
<html lang="en">
<head>
<meta charset="utf-8">
<title>Calderbrook Business Card</title>
<link rel="stylesheet" href="https://fonts.googleapis.com/css2?family=Marcellus&display=swap">
<style>
  :root {
    --navy: #1b2f7a;
    --navy-deep: #12215c;
    --green: #3f8f3a;
    --ink: #3b3b3b;
    --grey: #7a7a7a;
    --paper: #ffffff;
    --paper-shade: #eceef2;
    --backdrop: #d9dbe0;
  }
  * { margin: 0; padding: 0; box-sizing: border-box; }
  html, body { width: 1200px; height: 900px; overflow: hidden; }
  body {
    background: var(--backdrop);
    font-family: "Marcellus", Georgia, serif;
    display: flex;
    flex-direction: column;
    align-items: center;
    justify-content: center;
    gap: 60px;
  }
  .card {
    position: relative;
    width: 630px;
    height: 360px;
    overflow: hidden;
    box-shadow: 0 10px 28px rgba(0,0,0,0.18);
  }
  /* Front */
  .card-front {
    background: linear-gradient(160deg, var(--paper) 40%, var(--paper-shade) 100%);
  }
  .card-front .swoosh { position: absolute; inset: 0; }
  .wordmark {
    position: absolute;
    top: 30px;
    right: 40px;
    font-size: 40px;
    letter-spacing: 1px;
    color: var(--navy);
    line-height: 1;
  }
  .contact {
    position: absolute;
    top: 92px;
    right: 40px;
    text-align: right;
    color: var(--ink);
    font-size: 14px;
    line-height: 1.45;
  }
  .contact .address { margin-bottom: 8px; }
  .contact .line { display: flex; justify-content: flex-end; align-items: center; gap: 10px; }
  .contact .icon { width: 14px; height: 14px; flex: none; }
  .person { position: absolute; left: 46px; top: 170px; }
  .person .name { font-size: 24px; color: var(--navy); }
  .person .role { font-size: 17px; color: var(--grey); }
  .website {
    position: absolute;
    right: 40px;
    bottom: 70px;
    font-size: 20px;
    letter-spacing: 0.5px;
    color: var(--paper);
  }
  /* Back */
  .card-back {
    background: radial-gradient(ellipse at 60% 40%, #2a45a3 0%, var(--navy) 55%, var(--navy-deep) 100%);
    display: flex;
    align-items: center;
    justify-content: center;
  }
  .card-back .wordmark {
    position: static;
    font-size: 54px;
    color: var(--paper);
  }
</style>
</head>
<body>
  <section class="card card-front">
    <svg class="swoosh" viewBox="0 0 630 360" aria-hidden="true">
      <path d="M0,318 C210,314 420,255 630,188 L630,360 L0,360 Z" fill="var(--navy)"/>
      <path d="M0,296 C200,296 380,258 545,196 C395,262 205,310 0,312 Z" fill="var(--green)"/>
      <path d="M0,332 C220,330 430,268 630,200" fill="none" stroke="var(--paper)" stroke-width="2.5"/>
      <path d="M0,346 C200,344 360,312 520,262" fill="none" stroke="var(--paper)" stroke-width="1.5" opacity="0.8"/>
    </svg>

    <div class="wordmark">Calderbrook</div>

    <div class="contact">
      <div class="address">
        48 West 12th Street, 3rd Floor<br>
        New York, NY 10011
      </div>
      <div class="line">(07) 5531 2047
        <svg class="icon" viewBox="0 0 14 14" aria-hidden="true"><path d="M3 1 L5 1 L6 4 L4.5 5 C5.3 7 7 8.7 9 9.5 L10 8 L13 9 L13 11 C13 12 12 13 11 13 C6 13 1 8 1 3 C1 2 2 1 3 1 Z" fill="var(--ink)"/></svg>
      </div>
      <div class="line">(07) 5531 2048
        <svg class="icon" viewBox="0 0 14 14" aria-hidden="true"><rect x="3" y="1" width="8" height="4" fill="none" stroke="var(--ink)" stroke-width="1.3"/><rect x="1" y="5" width="12" height="6" rx="1" fill="var(--ink)"/><rect x="3.5" y="9" width="7" height="4" fill="var(--paper)" stroke="var(--ink)" stroke-width="1.2"/></svg>
      </div>
      <div class="line">martin@calderbrook.com
        <svg class="icon" viewBox="0 0 14 14" aria-hidden="true"><circle cx="7" cy="7" r="2.4" fill="none" stroke="var(--ink)" stroke-width="1.5"/><path d="M9.4 4.8 V8.2 C9.4 10 12.6 10 12.6 7 A5.6 5.6 0 1 0 10 11.8" fill="none" stroke="var(--ink)" stroke-width="1.5"/></svg>
      </div>
    </div>

    <div class="person">
      <div class="name">Martin Hale</div>
      <div class="role">President</div>
    </div>

    <div class="website">www.calderbrook.com</div>
  </section>

  <section class="card card-back">
    <div class="wordmark">Calderbrook</div>
  </section>
</body>
</html>
```